Poetry Book Cover Design Project

Looking for a minimalistic book cover design for a collection of poems. The book title is "Before The Morning Turns To Glass". There are three parts to the book. First covers poetry in the theme of Rage. Second love and desire. The third is strange poems. Essentially the sections are "Rage", "Desire" and the "Strange". The reason for the title "Before The Morning Turns To Glass" is as if someone is writing these till life changes towards the intended outcome as felt in each poem. I want to have the author's name "Nirosha Kulathunge" at the bottom. Ilustration attached.
- Minimalistic

```html
<!DOCTYPE html>
<html lang="en">
<head>
<meta charset="utf-8">
<title>Before The Morning Turns To Glass — Nirosha Kulathunge</title>
<link rel="stylesheet" href="https://fonts.googleapis.com/css2?family=Bebas+Neue&family=Oswald:wght@500&display=swap">
<style>
  :root {
    --cover-red: #b3111b;
    --silhouette-black: #000000;
    --type-white: #ffffff;
  }
  html, body {
    margin: 0;
    padding: 0;
    width: 800px;
    height: 1200px;
    overflow: hidden;
    background: var(--cover-red);
  }
  .cover {
    position: relative;
    width: 800px;
    height: 1200px;
    background: var(--cover-red);
    overflow: hidden;
  }
  .profile-silhouette {
    position: absolute;
    left: 0;
    top: 0;
    width: 800px;
    height: 1200px;
  }
  .title {
    position: absolute;
    right: 40px;
    top: 104px;
    margin: 0;
    display: flex;
    flex-direction: column;
    align-items: flex-end;
    font-family: "Bebas Neue", "Oswald", sans-serif;
    font-weight: 400;
    font-size: 170px;
    line-height: 140px;
    letter-spacing: 1px;
    color: var(--type-white);
    text-transform: uppercase;
  }
  .title-line {
    display: block;
  }
  .author {
    position: absolute;
    right: 40px;
    top: 1088px;
    margin: 0;
    font-family: "Oswald", sans-serif;
    font-weight: 500;
    font-size: 34px;
    line-height: 40px;
    color: var(--type-white);
  }
</style>
</head>
<body>
  <main class="cover">
    <svg class="profile-silhouette" viewBox="0 0 800 1200" role="img" aria-label="Black silhouette of a human head in profile facing right">
      <path fill="var(--silhouette-black)" d="M0 0 H120 C180 160 250 300 280 440 C300 560 300 700 290 820 C280 940 250 1060 210 1200 H0 Z"/>
    </svg>
    <h1 class="title">
      <span class="title-line">Before</span>
      <span class="title-line">The</span>
      <span class="title-line">Morning</span>
      <span class="title-line">Turns</span>
      <span class="title-line">To</span>
      <span class="title-line">Glass</span>
    </h1>
    <p class="author">Nirosha Kulathunge</p>
  </main>
</body>
</html>
```